Gift voucher with envelope and letterhead

Hi Marisol
I would like the voucher to be business envelope size
It will need to have:
to
from
amount
$
date
expiry date
Lantern Shelf
our phone     (02 6384 9017)
email     lanshe@tealnet.com
message     (with a space to add a personalised message)
also    'this voucher can be redeemed for goods only at Lantern Shelf'
I will have it printed on card so you could specify the colour card to print on
Then we will co-ordinate envelope
Envelope should have at least
Gift Voucher   printed on front
but maybe not the words lantern shelf but just something (maybe the book stack?....I don't know....you're the expert!!!!) that identifies us.
Could you also do a letterhead..... basic.....I don't think I will use it very often

```html
<!DOCTYPE html>
<html lang="en">
<head>
<meta charset="utf-8">
<title>Lantern Shelf – Gift Voucher Designs</title>
<link href="https://fonts.googleapis.com/css2?family=Advent+Pro:wght@300;400&family=Libre+Baskerville:wght@700&display=swap" rel="stylesheet">
<style>
  :root {
    --page: #f4f4f4;
    --card: #ffffff;
    --card-edge: #8a8a8a;
    --ink: #4a3a2c;
    --twine: #c79d5f;
    --twine-dark: #a97b3e;
    --field-edge: #6d6d6d;
    --dash: #b5a58d;
    --label: #222222;
  }
  * { box-sizing: border-box; margin: 0; padding: 0; }
  html, body { width: 1200px; height: 561px; overflow: hidden; background: var(--page); }
  .sheet { position: relative; width: 1200px; height: 561px; }

  .voucher {
    position: absolute; width: 529px; height: 227px;
    background: var(--card); border: 1px solid var(--card-edge); overflow: hidden;
  }
  .voucher--front-a { left: 37px; top: 28px; }
  .voucher--front-b { left: 639px; top: 28px; }
  .voucher--front-c { left: 37px; top: 308px; }
  .voucher--back   { left: 639px; top: 308px; }

  .voucher__title {
    position: absolute; font-family: "Advent Pro", sans-serif; font-weight: 300;
    font-size: 42px; color: var(--ink); line-height: 1; white-space: nowrap;
  }
  .voucher--front-a .voucher__title { left: 20px; top: 18px; }
  .voucher--front-b .voucher__title { left: 310px; top: 34px; }
  .voucher--front-c .voucher__title { left: 24px; top: 64px; }

  .title-rule {
    position: absolute; left: 275px; top: 88px; width: 225px; height: 0;
    border-top: 3px dashed var(--dash);
  }

  .twine {
    position: absolute; height: 4px; border-radius: 2px;
    background: linear-gradient(90deg, var(--twine), var(--twine-dark), var(--twine));
    transform-origin: left center;
  }
  .twine-bow {
    position: absolute; width: 80px; height: 80px; border-radius: 50%;
    background: radial-gradient(circle, rgba(199,157,95,.85) 0%, rgba(199,157,95,.35) 55%, rgba(199,157,95,0) 72%);
  }

  .book-stack { position: absolute; background: var(--ink); }
  .voucher--front-a .book-stack { left: 300px; top: 119px; width: 229px; height: 108px; }
  .voucher--front-b .book-stack { left: 305px; top: 119px; width: 224px; height: 108px; }
  .voucher--front-c .book-stack { left: 0; top: 124px; width: 240px; height: 103px; }
  .voucher--back .book-stack   { left: 5px; top: 155px; width: 80px; height: 62px; }

  .brand-name {
    position: absolute; font-family: "Advent Pro", sans-serif; font-weight: 400;
    color: var(--ink); text-transform: uppercase; line-height: 1; white-space: nowrap;
  }
  .voucher--front-a .brand-name { left: 92px; top: 182px; font-size: 30px; }
  .voucher--front-b .brand-name { left: 100px; top: 182px; font-size: 30px; }
  .voucher--front-c .brand-name { left: 254px; top: 182px; font-size: 30px; }
  .voucher--back .brand-name   { left: 92px; top: 188px; font-size: 19px; }

  .field-label {
    position: absolute; font-family: "Libre Baskerville", serif; font-weight: 700;
    font-size: 11px; color: var(--label); text-align: right; white-space: nowrap;
  }
  .field-label--left { right: 452px; }
  .field-label--right { right: 201px; }
  .field-label--small { font-size: 7.5px; }
  .field-box {
    position: absolute; border: 1px solid var(--field-edge); border-radius: 3px; background: var(--card);
  }

  .redeem-note {
    position: absolute; left: 270px; top: 160px; width: 250px;
    font-family: "Libre Baskerville", serif; font-weight: 700; font-size: 10px;
    line-height: 1.4; color: var(--label); text-align: center;
  }
  .back-rule {
    position: absolute; left: 250px; top: 201px; width: 275px; border-top: 2px dashed var(--dash);
  }
  .phone-line {
    position: absolute; left: 330px; top: 210px; width: 160px; text-align: center;
    font-family: "Libre Baskerville", serif; font-weight: 700; font-size: 7.5px; color: var(--label);
  }
</style>
</head>
<body>
<main class="sheet">

  <section class="voucher voucher--front-a">
    <div class="twine" style="left:0;top:72px;width:529px;" role="img" aria-label="Twine string across the card"></div>
    <div class="twine-bow" style="left:335px;top:34px;" role="img" aria-label="Tied twine bow"></div>
    <h2 class="voucher__title">gift voucher</h2>
    <div class="book-stack" role="img" aria-label="Row of standing books illustration"></div>
    <p class="brand-name">Lantern Shelf</p>
  </section>

  <section class="voucher voucher--front-b">
    <div class="twine" style="left:-10px;top:40px;width:560px;transform:rotate(-10deg);" role="img" aria-label="Twine string across the card"></div>
    <div class="twine" style="left:20px;top:-10px;width:260px;transform:rotate(70deg);" role="img" aria-label="Twine string crossing down the card"></div>
    <div class="twine-bow" style="left:40px;top:10px;" role="img" aria-label="Tied twine bow"></div>
    <h2 class="voucher__title">gift voucher</h2>
    <div class="title-rule"></div>
    <div class="book-stack" role="img" aria-label="Row of standing books illustration"></div>
    <p class="brand-name">Lantern Shelf</p>
  </section>

  <section class="voucher voucher--front-c">
    <div class="twine" style="left:0;top:12px;width:540px;transform:rotate(3deg);" role="img" aria-label="Twine string across the card"></div>
    <div class="twine-bow" style="left:330px;top:4px;" role="img" aria-label="Tied twine bow"></div>
    <h2 class="voucher__title">gift voucher</h2>
    <div class="book-stack" role="img" aria-label="Row of standing books illustration"></div>
    <p class="brand-name">Lantern Shelf</p>
  </section>

  <section class="voucher voucher--back">
    <div class="twine" style="left:0;top:58px;width:300px;transform:rotate(-22deg);" role="img" aria-label="Twine string across the corner"></div>

    <span class="field-label field-label--right field-label--small" style="top:10px;">Reference #</span>
    <div class="field-box" style="left:333px;top:5px;width:157px;height:19px;"></div>

    <span class="field-label field-label--left" style="top:48px;">To</span>
    <div class="field-box" style="left:83px;top:40px;width:159px;height:28px;"></div>
    <span class="field-label field-label--right" style="top:48px;">From</span>
    <div class="field-box" style="left:333px;top:40px;width:156px;height:28px;"></div>

    <span class="field-label field-label--left" style="top:84px;">Expires</span>
    <div class="field-box" style="left:83px;top:78px;width:159px;height:27px;"></div>
    <span class="field-label field-label--right" style="top:84px;">Amount</span>
    <div class="field-box" style="left:333px;top:78px;width:156px;height:27px;"></div>

    <span class="field-label field-label--left" style="top:124px;">Message</span>
    <div class="field-box" style="left:82px;top:117px;width:407px;height:27px;"></div>

    <p class="redeem-note">This voucher can be redeemed for goods only at Lantern Shelf.</p>
    <div class="back-rule"></div>
    <p class="phone-line">Phone - 02 6384 9017</p>

    <div class="book-stack" role="img" aria-label="Small row of standing books illustration"></div>
    <p class="brand-name">Lantern Shelf</p>
  </section>

</main>
</body>
</html>
```